Joomla Responsive Website Template for an International Biotechnology Company

Our client is a biotechnology company that uses silver-based technology to help make products antimicrobial, antibacterial, and anti fungal. We need a Joomla-based template that is responsive/mobile friendly when viewed on tablets or smartphones. We are looking for a template design for the home page and subpages. We are replacing the current website http://www.velmora-labs.com with a new website being built here: http://velmoraclean.com.stagehost.com/velmoraprime/. What we have now on the site is the basic wire frame. This is the desired layout and pictures we want to use. We would like you to add some design elements to make the website more professional looking and polished. Please refer to the attached style guide to help you in choosing the color. The client does like the green leaf, which is included in the last page of style guide and may be good for a background image. While the Velmora logo and leaf are green, we do not want to overuse the color green. The client does own other technologies that we will be promoting on the site and the logos for these technologies are attached below. These logos are Tusk, Velmora-Prime, and Wisp. We will be using this website to promote the technologies, the markets the technologies serve; drinking water, medical devices, apparel and textiles, and architectural surfaces, and to promote the customer using these devices. Please make the design "clean" and not cluttered, as these technologies are used to fight "dirty things".
Updates

Hello Designers! Thank you all very much for your design submissions. They were simply excellent. Due to the Holidays and New Years, many of the client's team members have been on vacation. We expect to have feedback shortly and pick the top design soon there after. Again, thank you all very much and hope the New Year brings you continued success. Best, Dorian

Industry/Entity Type

Biotechnology

Coding

Coded - Design and coding required

```html
<!DOCTYPE html>
<html lang="en">
<head>
<meta charset="utf-8">
<title>Velmora Antimicrobial</title>
<link rel="stylesheet" href="https://fonts.googleapis.com/css2?family=Open+Sans:wght@400;600;700&display=swap">
<style>
:root{
  --green:#7dc142;
  --green-dark:#5fa32c;
  --text:#3a3a3a;
  --muted:#777;
  --band:#f3f3f3;
  --line:#b9b9b9;
  --social:#2d8fd0;
  --social-dark:#27428a;
}
*{box-sizing:border-box;margin:0;padding:0}
html,body{width:823px;height:1200px;overflow:hidden;background:#fff}
body{position:relative;font-family:"Open Sans",Arial,sans-serif;color:var(--text)}
.abs{position:absolute}
.brand{left:81px;top:8px;font-size:44px;font-weight:700;color:var(--green);letter-spacing:-1px;line-height:50px}
.search{left:510px;top:19px;width:162px;height:23px;border:1px solid #c8c8c8;font-size:11px;padding:4px 9px;color:#444}
.search svg{position:absolute;right:8px;top:4px}
.social{top:16px;width:27px;height:27px;border-radius:3px}
.social.one{left:684px;background:var(--social)}
.social.two{left:713px;background:var(--social-dark)}
.nav{left:81px;top:68px;width:659px;height:18px;border-bottom:1px solid var(--line)}
.nav a{position:absolute;top:0;font-size:11px;color:var(--muted);text-decoration:none;line-height:16px}
.nav a.active{background:var(--green);color:#fff;padding:0 5px}
.hero{left:81px;top:98px;width:659px;height:268px;
  background:
    radial-gradient(ellipse 18% 30% at 22% 30%,rgba(40,110,220,.55),transparent 70%),
    radial-gradient(ellipse 40% 30% at 55% 85%,rgba(255,255,255,.55),transparent 70%),
    linear-gradient(135deg,#e4ecfc 0%,#a9bff2 40%,#7b9be8 65%,#cfdbf8 100%)}
.section-title{left:0;width:823px;top:386px;text-align:center;font-size:18px;font-weight:700}
.market{top:422px;width:153px}
.market h3{font-size:11.5px;font-weight:600;text-align:center;margin-bottom:5px}
.market .photo{height:143px}
.market p{font-size:8.6px;line-height:10px;margin-top:3px;padding-left:1px;color:#222}
.market a{font-size:8.6px;color:var(--green-dark);display:block;text-decoration:underline}
.band{left:0;top:648px;width:823px;height:177px;background:var(--band)}
.leaf{left:567px;top:651px;width:256px;height:168px;background:radial-gradient(ellipse at 60% 45%,#c4e46a 0%,#92c83e 50%,#5a9e26 100%);border-radius:60% 0 0 70%/70% 0 0 60%}
.about h2{font-size:20.5px;font-weight:600;position:absolute;left:81px;top:663px}
.about h2 sup{font-size:11px}
.about p{position:absolute;left:81px;top:699px;width:480px;font-size:10.5px;line-height:17.8px;color:#444}
.col-title{top:849px;font-size:17.5px;font-weight:600}
.news{left:81px;top:883px;width:300px;list-style:none}
.news li{font-size:10.8px;line-height:15.5px;margin-bottom:9px;color:#333}
.quote{left:435px;top:883px;width:305px;font-size:10.3px;line-height:15.9px;color:#333}
.author{left:633px;top:1004px;font-size:10.5px;line-height:12px}
.author b{display:block;font-weight:700}
.partner{top:1093px;height:27px;border-radius:3px}
.footer-line{left:81px;top:1151px;width:662px;border-top:2px solid var(--green)}
.footer-brand{left:88px;top:1162px;font-size:13px;font-weight:700;color:var(--green);line-height:16px}
.footer-nav a{position:absolute;top:1165px;font-size:9.5px;color:var(--muted);text-decoration:none}
</style>
</head>
<body>
<header>
  <div class="abs brand">velmora</div>
  <div class="abs search">Search ...
    <svg width="16" height="14" viewBox="0 0 16 14"><circle cx="6" cy="6" r="4.5" fill="none" stroke="#777" stroke-width="1.6"/><line x1="9.5" y1="9" x2="14.5" y2="13" stroke="#777" stroke-width="2"/></svg>
  </div>
  <div class="abs social one" role="img" aria-label="Social network link"></div>
  <div class="abs social two" role="img" aria-label="Social network link"></div>
  <nav class="abs nav">
    <a style="left:7px">Home</a>
    <a style="left:79px">About Us</a>
    <a style="left:165px">Markets</a>
    <a class="active" style="left:241px">Technology</a>
    <a style="left:344px">Customer Programs</a>
    <a style="left:479px">News Highlights</a>
    <a style="left:597px">Contact Us</a>
  </nav>
</header>

<div class="abs hero" role="img" aria-label="Pipette dropping blue liquid into laboratory test tubes"></div>

<h2 class="abs section-title">Our Markets</h2>
<div class="abs market" style="left:82px">
  <h3>Drinking Water</h3>
  <div class="photo" role="img" aria-label="Water filter pitcher" style="background:radial-gradient(ellipse 45% 55% at 45% 55%,rgba(200,215,235,.55),transparent 70%),linear-gradient(160deg,#3c6fb0,#0f2f6a)"></div>
  <p>Lorem ipsum dolor sit amet, consec sit tetur adipiscing elit sed do.</p><a>Learn More</a>
</div>
<div class="abs market" style="left:250px">
  <h3>Medical Devices</h3>
  <div class="photo" role="img" aria-label="Nurse with patient in hospital room" style="background:radial-gradient(ellipse 50% 30% at 50% 85%,rgba(255,255,255,.8),transparent 70%),linear-gradient(160deg,#dfe9f2,#9fb6c9)"></div>
  <p>Lorem ipsum dolor sit amet, consec sit tetur adipiscing elit sed do.</p><a>Learn More</a>
</div>
<div class="abs market" style="left:418px">
  <h3>Apparel &amp; Textiles</h3>
  <div class="photo" role="img" aria-label="Stack of folded fabrics" style="background:linear-gradient(180deg,#8a8c92 0%,#4d5058 35%,#2f5fa4 70%,#8aa3c4 100%)"></div>
  <p>Lorem ipsum dolor sit amet, consec sit tetur adipiscing elit sed do.</p><a>Learn More</a>
</div>
<div class="abs market" style="left:587px">
  <h3>Architectural Surfaces</h3>
  <div class="photo" role="img" aria-label="Laboratory benches with equipment" style="background:linear-gradient(160deg,#f4f2ec,#c9c5b8)"></div>
  <p>Lorem ipsum dolor sit amet, consec sit tetur adipiscing elit sed do.</p><a>Learn More</a>
</div>

<section class="about">
  <div class="abs band"></div>
  <div class="abs leaf" role="img" aria-label="Green leaf"></div>
  <h2>Velmora<sup>®</sup> Antimicrobial</h2>
  <p>Velmora branded antimicrobial technology makes products cleaner and longer lasting with silver, copper and zinc, which have been proven in use throughout history. Velmora antimicrobial technology provides built-in protection by working 24/7 resisting the growth of microbes. We work in close partnership with our customers, from development to end-user marketing, to deliver a product advantage that makes a real difference in the marketplace. *Velmora is an EPA registered ionic silver technology and is not a nanosilver technology.</p>
</section>

<h2 class="abs col-title" style="left:81px">News &amp; Events</h2>
<ul class="abs news">
  <li>New Council for Clinical Hygiene Standards (CCHS) Guidelines Include Velmora Antimicrobial-Treated Catheters</li>
  <li>Harborline Marathon Winner Wears Strideway Shoes Protected by Velmora Antimicrobial</li>
  <li>Quellon Strengthens and Expands Technical Sales and Services Efforts with New Hire in West Asia(2)</li>
  <li>Fenwick's Chooses Velmora Prime to Deliver Odor Elimination Benefits</li>
</ul>

<h2 class="abs col-title" style="left:435px">Testimonials</h2>
<p class="abs quote">Contrary to popular belief, Lorem Ipsum is not simply random text. It has roots in a piece of classical Latin literature from 45 BC, making it over 2000 years old. Edwin Hartwell, a Latin professor at Ashgrove College in Virginia, looked up one of the more obscure Latin words, consectetur, from a Lorem Ipsum passage, and going through the cites of the word in classical literature, discovered the undoubtable source.</p>
<div class="abs author"><b>John Doe Smith</b>CEO, Mc Dowald</div>

<div class="abs partner" style="left:81px;width:102px;background:#1d4f9c"></div>
<div class="abs partner" style="left:211px;width:96px;background:#2c8fd0"></div>
<div class="abs partner" style="left:332px;width:84px;background:#2a3b7a"></div>
<div class="abs partner" style="left:441px;width:69px;background:#111"></div>
<div class="abs partner" style="left:535px;width:105px;background:#555"></div>
<div class="abs partner" style="left:664px;width:76px;background:#e6c51f"></div>

<footer>
  <div class="abs footer-line"></div>
  <div class="abs footer-brand">velmora</div>
  <nav class="footer-nav">
    <a style="left:154px">Home</a>
    <a style="left:201px">About Us</a>
    <a style="left:260px">Markets</a>
    <a style="left:313px">Technology</a>
    <a style="left:384px">Customer Programs</a>
    <a style="left:485px">News Highlights</a>
    <a style="left:573px">Contact Us</a>
  </nav>
</footer>
</body>
</html>
```